Hello,

I would like to recieve a template that i can use for:

Presentation folders
pdf files
word files

Logo, fond and colors are included in attachment.

Target Market(s)

Small Business

Requirements
Must have
• clean and simple

```html
<!DOCTYPE html>
<html lang="en">
<head>
<meta charset="utf-8">
<title>TaskEase Stationery Templates</title>
<link href="https://fonts.googleapis.com/css2?family=Mulish:wght@400;600&display=swap" rel="stylesheet">
<style>
  :root {
    --board: #444444;
    --paper: #ffffff;
    --green: #8bc043;
    --green-deep: #80b13f;
    --blue: #29a8e0;
    --blue-pale: #cde9f8;
    --tab: #2b92c4;
    --ink: #555555;
  }
  * { margin: 0; padding: 0; box-sizing: border-box; }
  html, body { width: 1200px; height: 1000px; overflow: hidden; }
  body {
    background: var(--board);
    font-family: "Mulish", "Helvetica Neue", Arial, sans-serif;
    position: relative;
  }
  .tab {
    position: absolute;
    background: var(--tab);
    color: #fff;
    font-size: 14px;
    font-weight: 600;
    display: flex; align-items: center; justify-content: center;
    white-space: nowrap;
  }
  .sheet { position: absolute; background: var(--paper); box-shadow: 0 6px 18px rgba(0,0,0,.35); overflow: hidden; }
  .brand { position: absolute; display: flex; align-items: center; gap: 8px; }
  .brand-mark { background: var(--blue); border-radius: 3px; }
  .brand-name { color: var(--green); font-weight: 600; }
  .web { position: absolute; color: var(--blue); font-size: 10px; display: flex; align-items: center; gap: 4px; }
  .web-dot { width: 7px; height: 7px; border-radius: 50%; background: var(--green); }

  /* Letterhead */
  .letterhead { left: 17px; top: 81px; width: 589px; height: 832px; }
  .letterhead .brand { left: 31px; top: 38px; }
  .letterhead .brand-mark { width: 30px; height: 30px; }
  .letterhead .brand-name { font-size: 26px; }
  .letterhead .web { left: 420px; top: 45px; }
  .letterhead .emblem { position: absolute; left: 70px; top: 600px; width: 120px; height: 120px; border-radius: 50%; background: var(--blue-pale); opacity: .8; }
  .contact { position: absolute; left: 40px; top: 737px; font-size: 8px; color: var(--ink); }
  .contact-name { color: var(--blue); font-size: 12px; margin: 0 0 6px 10px; }
  .contact-row { display: flex; align-items: center; gap: 9px; height: 14px; }
  .letterhead .swoosh { position: absolute; left: 0; bottom: 0; }

  /* PDF cover */
  .pdf-cover { left: 383px; top: 222px; width: 520px; height: 732px; transform: rotate(4.2deg); overflow: visible; background: transparent; box-shadow: none; }
  .pdf-face { position: absolute; inset: 0; background: var(--green); box-shadow: 0 6px 18px rgba(0,0,0,.35); overflow: hidden; }
  .pdf-cover .tab { right: 0; top: -30px; width: 178px; height: 32px; }
  .pdf-cover .brand { left: 225px; top: 190px; }
  .pdf-cover .brand-mark { width: 28px; height: 28px; background: #fff; }
  .pdf-cover .brand-name { color: #fff; font-size: 24px; }
  .pdf-cover .web { left: 210px; top: 612px; color: #fff; }
  .pdf-cover .web-dot { background: #fff; }
  .pdf-emblem { position: absolute; left: 355px; top: 110px; width: 170px; height: 170px; border-radius: 50%; border: 12px solid var(--green-deep); }

  /* Slide */
  .slide { left: 756px; top: 548px; width: 426px; height: 328px; }
  .slide-tab { left: 1032px; top: 521px; width: 150px; height: 27px; }
  .slide .brand { left: 16px; top: 24px; gap: 6px; }
  .slide .brand-mark { width: 20px; height: 20px; }
  .slide .brand-name { font-size: 17px; }
  .slide .web { left: 306px; top: 31px; font-size: 8px; }
  .slide-title { position: absolute; left: 34px; top: 112px; color: var(--blue); font-size: 30px; font-weight: 400; }
  .slide-rule { position: absolute; left: 34px; top: 146px; width: 284px; height: 1px; background: var(--blue); }
  .slide-rule::after { content: ""; position: absolute; right: -2px; top: -2px; width: 5px; height: 5px; border-radius: 50%; background: var(--blue); }
  .slide-sub { position: absolute; left: 36px; top: 152px; color: var(--green); font-size: 12.5px; }
  .slide .emblem { position: absolute; left: 20px; top: 228px; width: 72px; height: 72px; border-radius: 50%; background: var(--blue-pale); opacity: .8; }
  .slide .swoosh { position: absolute; left: 0; bottom: 0; }
</style>
</head>
<body>

  <div class="tab" style="left:427px; top:44px; width:179px; height:37px;">Letterhead word Template</div>
  <section class="sheet letterhead">
    <div class="brand"><span class="brand-mark"></span><span class="brand-name">TaskEase</span></div>
    <div class="web"><span class="web-dot"></span>www.taskease-site.com</div>
    <div class="emblem" role="img" aria-label="Faint brand emblem watermark"></div>
    <div class="contact">
      <p class="contact-name">Task Ease</p>
      <p class="contact-row">
        <svg width="8" height="10" viewBox="0 0 8 10"><path d="M4 0a4 4 0 0 1 4 4c0 3-4 6-4 6S0 7 0 4a4 4 0 0 1 4-4z" fill="#8bc043"/><circle cx="4" cy="4" r="1.5" fill="#fff"/></svg>
        Company address</p>
      <p class="contact-row">
        <svg width="9" height="9" viewBox="0 0 10 10"><circle cx="5" cy="5" r="4.3" fill="none" stroke="#8bc043" stroke-width="1.2"/><path d="M3.3 3.2l1 .2.3 1-.5.5a3 3 0 0 0 1.2 1.2l.5-.5 1 .3.2 1C5.5 7 3 5.5 3.3 3.2z" fill="#8bc043"/></svg>
        0000 0000 00</p>
      <p class="contact-row">
        <svg width="10" height="8" viewBox="0 0 10 8"><rect x=".5" y=".5" width="9" height="7" fill="none" stroke="#8bc043"/><path d="M.5 .5L5 4.5 9.5.5" fill="none" stroke="#8bc043"/></svg>
        hello@taskease-mail.com</p>
    </div>
    <svg class="swoosh" width="589" height="16" viewBox="0 0 589 16"><path d="M0 8 Q300 10 589 0 V16 H0z" fill="#8bc043"/></svg>
  </section>

  <section class="sheet pdf-cover">
    <div class="pdf-face">
      <svg width="520" height="732" viewBox="0 0 520 732" style="position:absolute;left:0;top:0">
        <path d="M140 0 H520 V430 H210 Q110 430 110 500 V460 Q110 520 170 520 H370 V520 H180 Q110 515 110 450 Z" fill="#80b13f"/>
        <path d="M140 0 H520 V520 H180 Q110 520 110 450 V0 Z" fill="#80b13f"/>
        <path d="M250 40 H520 V410 H310 Q260 410 260 370 Z" fill="none"/>
        <rect x="210" y="40" width="340" height="370" rx="42" fill="#8bc043"/>
      </svg>
      <div class="pdf-emblem" role="img" aria-label="Faint brand emblem watermark"></div>
      <div class="brand"><span class="brand-mark"></span><span class="brand-name">TaskEase</span></div>
      <div class="web"><span class="web-dot"></span>www.taskease-site.com</div>
    </div>
    <div class="tab">PDF&nbsp; Template</div>
  </section>

  <div class="tab slide-tab">Powerpoint Template</div>
  <section class="sheet slide">
    <div class="brand"><span class="brand-mark"></span><span class="brand-name">TaskEase</span></div>
    <div class="web"><span class="web-dot"></span>www.taskease-site.com</div>
    <h1 class="slide-title">Insert the title</h1>
    <div class="slide-rule"></div>
    <p class="slide-sub">Sample text for subtitle</p>
    <div class="emblem" role="img" aria-label="Faint brand emblem watermark"></div>
    <svg class="swoosh" width="426" height="52" viewBox="0 0 426 52"><path d="M0 50 Q250 50 426 0 V52 H0z" fill="#8bc043"/></svg>
  </section>

</body>
</html>
```